" RADIANT SPRINGTIDE 2020 ".

I want a flyer to invite people to a 2 Days Miracle Service. Salvation, Deliverance, Healing, Restoration, Breakthrough .
The best flyer you can propose me. Insert the logo i send you on the flyer. 04/11-04/12/2020. From 6:00Pm-10:00Pm. Venue: 5:00Pm. With Evangelist PAUL-HENRI MBOTELA. ( FLAME & RIVER Ministry ) At: Westbrook Harmony Hall. 24615 LANVER Street, Romulus, Michigan 48296. Jesus-Christ Is the Lord.
Contact: - email : flameriverfellow@examplemail.test
- cell phone: 5907214836
- Whatsapp :5907214836

Target Market(s)

Michigan, all ages

Font styles to use
Decorative
Script

Requirements
Must have
• Must have the logo of the ministry.

```html
<!DOCTYPE html>
<html lang="en">
<head>
<meta charset="utf-8">
<title>Radiant Springtide 2020 – 2 Days Miracle Service</title>
<link href="https://fonts.googleapis.com/css2?family=Oswald:wght@500&family=Open+Sans:wght@400;700&family=Parisienne&family=Great+Vibes&display=swap" rel="stylesheet">
<style>
  :root {
    --bg-dark: #2e2a2a;
    --red: #b8281f;
    --stripe: #c2412a;
    --accent-pink: #d0195a;
    --brand-red: #e2353a;
    --brand-blue: #3d6aa8;
    --white: #ffffff;
  }
  html, body {
    margin: 0;
    width: 1043px;
    height: 1200px;
    overflow: hidden;
    background: var(--bg-dark);
  }
  .flyer {
    position: relative;
    width: 1043px;
    height: 1200px;
    overflow: hidden;
    font-family: "Open Sans", Arial, sans-serif;
    color: var(--white);
  }
  .backdrop { position: absolute; inset: 0; }
  .brand {
    position: absolute;
    left: 120px;
    top: 26px;
    width: 250px;
    text-align: center;
  }
  .brand-mark {
    width: 220px;
    height: 220px;
    border-radius: 50%;
    background: var(--brand-blue);
    margin: 0 auto 38px;
  }
  .brand-name {
    font-weight: 700;
    font-size: 20px;
    line-height: 1.15;
    color: var(--brand-red);
  }
  .right { position: absolute; right: 34px; margin: 0; text-align: right; }
  .event-season {
    top: 55px;
    font-family: "Oswald", Impact, sans-serif;
    font-weight: 500;
    font-size: 29px;
    letter-spacing: 0.3px;
  }
  .event-title {
    top: 155px;
    font-family: "Oswald", Impact, sans-serif;
    font-weight: 500;
    font-size: 48px;
    line-height: 1;
  }
  .event-themes {
    top: 222px;
    font-family: "Parisienne", cursive;
    font-size: 32px;
    line-height: 1.3;
  }
  .event-schedule {
    top: 362px;
    font-size: 31px;
    line-height: 1.55;
  }
  .speaker { top: 560px; }
  .speaker-intro { font-size: 33px; line-height: 1.2; }
  .speaker-name { font-weight: 700; font-size: 31px; line-height: 1.3; }
  .speaker-ministry { font-weight: 700; font-size: 16px; }
  .venue {
    top: 700px;
    font-weight: 700;
    font-size: 21px;
    line-height: 1.3;
  }
  .proclamation {
    position: absolute;
    left: 0;
    right: 60px;
    top: 945px;
    margin: 0;
    text-align: center;
    font-family: "Great Vibes", cursive;
    font-size: 84px;
    line-height: 1;
    text-shadow: 0 2px 6px rgba(0,0,0,0.5);
  }
  .contacts {
    position: absolute;
    left: 50px;
    right: 40px;
    top: 1112px;
    display: flex;
    justify-content: space-between;
    font-size: 21px;
  }
  .contact { display: flex; align-items: center; gap: 10px; }
  .contact svg { width: 24px; height: 24px; }
</style>
</head>
<body>
<main class="flyer">
  <svg class="backdrop" width="1043" height="1200" viewBox="0 0 1043 1200">
    <defs>
      <linearGradient id="bgGrad" x1="0" y1="0" x2="1" y2="1">
        <stop offset="0" stop-color="#3c3535"/>
        <stop offset="1" stop-color="#231f1f"/>
      </linearGradient>
      <linearGradient id="headerGrad" x1="0" y1="0" x2="0" y2="1">
        <stop offset="0" stop-color="#4a0f0d"/>
        <stop offset="1" stop-color="#8f1d16"/>
      </linearGradient>
      <linearGradient id="titleGrad" x1="0" y1="0" x2="1" y2="0">
        <stop offset="0" stop-color="#c0301f"/>
        <stop offset="1" stop-color="#e35b40"/>
      </linearGradient>
      <linearGradient id="skyGrad" x1="0" y1="0" x2="0" y2="1">
        <stop offset="0" stop-color="#8a2a1c"/>
        <stop offset="0.45" stop-color="#c9866a"/>
        <stop offset="0.8" stop-color="#d98a3e"/>
        <stop offset="1" stop-color="#3a1e14"/>
      </linearGradient>
      <radialGradient id="speakerGrad" cx="0.5" cy="0.55" r="0.6">
        <stop offset="0" stop-color="#8c2a30" stop-opacity="0.85"/>
        <stop offset="0.6" stop-color="#3e3a4c" stop-opacity="0.7"/>
        <stop offset="1" stop-color="#2e2a2a" stop-opacity="0"/>
      </radialGradient>
      <linearGradient id="footerGrad" x1="0" y1="0" x2="0" y2="1">
        <stop offset="0" stop-color="#3a3636"/>
        <stop offset="1" stop-color="#121010"/>
      </linearGradient>
    </defs>

    <rect class="panel-base" width="1043" height="1200" fill="url(#bgGrad)"/>

    <path class="sky-photo" role="img" aria-label="Photo: sunset sky over a hill with three crosses"
          d="M490 330 L1043 330 L1043 1060 L450 1060 Q455 640 490 330 Z" fill="url(#skyGrad)"/>

    <path class="header-band" d="M548 0 L1043 0 L1043 330 L512 330 Q525 150 548 0 Z" fill="url(#headerGrad)"/>
    <path class="title-band" d="M530 110 L1043 110 L1043 330 L512 330 Q518 210 530 110 Z" fill="url(#titleGrad)"/>

    <path class="curve-stripe" d="M548 0 L568 0 Q520 420 470 1060 L448 1060 Q498 420 548 0 Z" fill="var(--stripe)"/>

    <rect class="speaker-photo" role="img" aria-label="Photo: the evangelist in a dark blazer and red shirt, one hand raised, singing into a microphone"
          x="20" y="350" width="610" height="720" fill="url(#speakerGrad)"/>

    <path class="footer" d="M0 1050 Q520 1100 1043 1030 L1043 1200 L0 1200 Z" fill="url(#footerGrad)"/>
    <path class="footer-line" d="M0 1050 Q520 1100 1043 1030" fill="none" stroke="var(--accent-pink)" stroke-width="5"/>
  </svg>

  <div class="brand">
    <div class="brand-mark"></div>
    <div class="brand-name">FLAME &amp; RIVER<br>Ministries</div>
  </div>

  <p class="right event-season">RADIANT SPRINGTIDE 2020</p>
  <h1 class="right event-title">2 DAYS MIRACLE SERVICE</h1>
  <p class="right event-themes">Salvation, Deliverance,<br>Healing, Restoration, Breakthrough</p>

  <p class="right event-schedule">04/11-04/12/2020.<br>From 6:00Pm-10:00Pm<br>Venue: 5:00Pm.</p>

  <div class="right speaker">
    <div class="speaker-intro">With Evangelist</div>
    <div class="speaker-name">PAUL-HENRI MBOTELA</div>
    <div class="speaker-ministry">( FLAME &amp; RIVER Ministry )</div>
  </div>

  <p class="right venue">At: Westbrook<br>Harmony Hall.<br>24615 LANVER Street, Romulus,<br>Michigan 48296.</p>

  <p class="proclamation">Jesus-Christ Is the Lord</p>

  <footer class="contacts">
    <span class="contact contact-email">
      <svg viewBox="0 0 24 24" aria-hidden="true"><path d="M3 9 L12 3 L21 9 V20 H3 Z M3 9 L12 15 L21 9" fill="none" stroke="#e2353a" stroke-width="2.2" stroke-linejoin="round"/></svg>
      flameriverfellow@examplemail.test
    </span>
    <span class="contact contact-phone">
      <svg viewBox="0 0 24 24" aria-hidden="true"><rect x="6" y="2" width="12" height="20" rx="2" fill="none" stroke="#e2353a" stroke-width="2.2"/><line x1="10" y1="18" x2="14" y2="18" stroke="#e2353a" stroke-width="2"/></svg>
      5907214836
    </span>
    <span class="contact contact-chat">
      <svg viewBox="0 0 24 24" aria-hidden="true"><circle cx="12" cy="12" r="9" fill="none" stroke="#e2353a" stroke-width="2.2"/><path d="M9 9 Q9 15 15 15" fill="none" stroke="#e2353a" stroke-width="2"/></svg>
      5907214836
    </span>
  </footer>
</main>
</body>
</html>
```